Project Management Software Brochure for Milestone Linked Tracking (MLT)

Our company has developed project management software (Milestone Linked Tracking - MLT) that we would like to start marketing commercially and would like to design a brochure to describe our product. The brochure must use a theme consistent with our company website (www.velstrafield.com) and use some of the material from the attached powerpoint presentation. Ideally the brochure should be foldable and no more that 2 sides of an A4. Our company is a project controls consultancy and there is a lot of information about us on our website. The brochure is for the software though and not the company. Attached are also some sample output report graphics. Please crop and size to suit.

Target Market(s)

All projects across all industries including Civil, Infrastructure, IT, Oil & Gas, Telecommunications, Power, Pipeline across the globe. Basically any project can use this software and help it to deliver a successful project within budget and on schedule.

Industry/Entity Type

Marketing

Font styles to use
Serif
Sans Serif

Requirements
Must have
• The same (or similar) theme to the company website (www.velstrafield.com). It must be a marketing brochure aimed at capturing potential customers attention. It should have a good balance of text versus graphics. It should also have a reference to our website and a contact details section.
Nice to have
• Must be visual to attract attention.

```html
<!DOCTYPE html>
<html lang="en">
<head>
<meta charset="utf-8">
<title>Milestone Linked Tracking (MLT) – Brochure</title>
<link rel="stylesheet" href="https://fonts.googleapis.com/css2?family=Open+Sans:wght@400;600;700;800&display=swap">
<style>
  :root {
    --page-bg: #dcdcde;
    --paper: #efeeec;
    --brand-blue: #2d5fae;
    --brand-blue-light: #4a7cc9;
    --text: #4a4a4a;
    --title: #3a3a3a;
    --band-dark: #2b2b2d;
    --chart-pink: #e0557a;
    --chart-green: #8fcf7a;
    --chart-yellow: #f2d46a;
    --chart-red: #e8766a;
  }
  * { box-sizing: border-box; margin: 0; padding: 0; }
  html, body { width: 1200px; height: 839px; overflow: hidden; }
  body {
    background: var(--page-bg);
    font-family: "Open Sans", Arial, sans-serif;
    color: var(--text);
    position: relative;
  }
  .panel {
    position: absolute;
    top: 60px;
    width: 370px;
    height: 720px;
    background: var(--paper);
    border-top: 6px solid var(--brand-blue);
    border-bottom: 6px solid var(--brand-blue);
    box-shadow: 0 6px 18px rgba(0,0,0,.18);
  }
  .panel--text { left: 30px; padding: 36px 34px; }
  .panel--charts { left: 415px; padding: 30px 26px; }
  .panel--cover { left: 800px; }

  .section-title {
    color: var(--brand-blue);
    font-weight: 600;
    font-size: 20px;
    line-height: 1.15;
    text-transform: uppercase;
    margin-bottom: 14px;
  }
  .body-copy { font-size: 11.5px; line-height: 1.55; margin-bottom: 14px; }
  .list-title {
    color: var(--brand-blue);
    font-weight: 700;
    font-size: 11.5px;
    text-transform: uppercase;
    margin-bottom: 4px;
  }
  .bullet-list { font-size: 11.5px; line-height: 1.55; padding-left: 16px; margin-bottom: 22px; }
  .dot-divider { display: flex; gap: 5px; margin: 6px 0 26px; }
  .dot-divider span { width: 6px; height: 6px; border-radius: 50%; background: var(--brand-blue-light); opacity: .8; }
  .dot-divider span:nth-child(n+6) { opacity: .35; }

  .chart-card {
    position: relative;
    background: #fff;
    border-top: 3px solid #222;
    height: 150px;
    margin-bottom: 16px;
    box-shadow: 0 1px 3px rgba(0,0,0,.12);
  }
  .chart-card svg { width: 100%; height: 100%; display: block; }
  .chart-badge {
    position: absolute;
    left: -18px;
    width: 62px; height: 62px;
    border-radius: 50%;
    background: var(--brand-blue);
    color: #fff;
    font-size: 9px;
    font-weight: 700;
    text-align: center;
    display: flex; align-items: center; justify-content: center;
    line-height: 1.1;
    z-index: 2;
  }
  .chart-badge--pareto { top: 14px; }
  .chart-badge--trend { top: 520px; }

  .brand {
    position: absolute;
    top: 30px; right: 26px;
    display: flex; align-items: center; gap: 8px;
  }
  .brand-mark { width: 26px; height: 26px; border-radius: 50%; background: var(--brand-blue); }
  .brand-name { font-size: 14px; font-weight: 600; color: var(--title); text-transform: uppercase; letter-spacing: 1px; line-height: 1.15; }
  .cover-photo {
    position: absolute;
    top: 80px; left: 0; right: 0; height: 360px;
    background:
      radial-gradient(ellipse 45% 35% at 75% 30%, rgba(230,120,110,.45), transparent 70%),
      radial-gradient(ellipse 40% 30% at 55% 75%, rgba(40,40,42,.75), transparent 70%),
      linear-gradient(100deg, #4e5356 0%, #8d8f8f 22%, #e6dfd0 48%, #f4efe4 65%, #cdb59a 88%, #a98d72 100%);
  }
  .cover-band { position: absolute; top: 440px; left: 0; right: 0; height: 14px; background: var(--band-dark); }
  .cover-title {
    position: absolute;
    top: 478px; left: 0; right: 0;
    text-align: center;
    font-size: 27px;
    font-weight: 800;
    line-height: 1.2;
    text-transform: uppercase;
    color: var(--title);
  }
  .cover-title .accent { color: var(--brand-blue); }
  .cover-dots { position: absolute; top: 570px; left: 0; right: 0; display: flex; justify-content: center; gap: 5px; }
  .cover-dots span { width: 6px; height: 6px; border-radius: 50%; background: var(--brand-blue-light); }
  .cover-dots span:nth-child(n+5) { opacity: .4; }
  .cover-subtitle {
    position: absolute; top: 590px; left: 0; right: 0;
    text-align: center;
    font-size: 14px; font-weight: 700; letter-spacing: .5px;
    text-transform: uppercase;
    color: var(--brand-blue);
  }
  .cover-contact {
    position: absolute; left: 0; right: 0; bottom: 22px;
    text-align: center;
    font-size: 11px; line-height: 1.6;
    color: var(--text);
  }
  .cover-contact strong { color: var(--brand-blue); font-weight: 700; }
</style>
</head>
<body>

<section class="panel panel--text">
  <h2 class="section-title">Deliverable Based<br>Approach</h2>
  <p class="body-copy">There are usually significant deliverables that need to be produced. Deliverables may be contractual (customer) or internal requirements. These may consist of purchase orders, sub contract formation logs, drawings, specifications, reports, procedures, test results etc. Volume and complexity make it difficult to determine meaningful interdependencies. CPM is not the most effective methodology for managing the progress and performance of these deliverables. Deliverables are tracked at a lower level than the CPM schedules in numerous spreadsheets.</p>
  <h3 class="list-title">Spreadsheets tend to:</h3>
  <ul class="bullet-list">
    <li>have limited version control</li>
    <li>are susceptible to constant change</li>
    <li>do not promote a disciplined approach to progress and performance monitoring</li>
  </ul>
  <div class="dot-divider"><span></span><span></span><span></span><span></span><span></span><span></span><span></span><span></span></div>
  <h2 class="section-title">MLT Methodology</h2>
  <p class="body-copy">Based on the principles of Earned Value Methodology (EVM). Progress/performance of deliverables in all project phases. Schedule Progress Index (SPI) and Cost Performance Index (CPI). Structured database that promotes discipline, structure and rigor. Effective performance measurement and feedback tools for projects. Patterns/trends in the past are accepted as good indicators of the future. Enables projects to integrate the management of scope, time and cost.</p>
</section>

<section class="panel panel--charts">
  <div class="chart-badge chart-badge--pareto">PARETO<br>CHART</div>
  <div class="chart-badge chart-badge--trend">TREND<br>CHART</div>

  <div class="chart-card">
    <svg viewBox="0 0 318 147" preserveAspectRatio="none">
      <g fill="var(--chart-pink)">
        <rect x="150" y="20" width="130" height="6"/><rect x="160" y="32" width="115" height="6"/>
        <rect x="170" y="44" width="100" height="6"/><rect x="178" y="56" width="88" height="6"/>
        <rect x="186" y="68" width="74" height="6"/><rect x="194" y="80" width="60" height="6"/>
      </g>
      <g fill="var(--chart-green)">
        <rect x="200" y="92" width="50" height="6"/><rect x="206" y="104" width="40" height="6"/>
      </g>
      <polyline points="20,130 80,110 140,80 200,50 290,25" fill="none" stroke="#444" stroke-width="1.2"/>
      <line x1="20" y1="130" x2="300" y2="130" stroke="#999"/>
    </svg>
  </div>

  <div class="chart-card">
    <svg viewBox="0 0 318 147" preserveAspectRatio="none">
      <line x1="10" y1="73" x2="308" y2="73" stroke="#bbb"/>
      <line x1="159" y1="8" x2="159" y2="140" stroke="#bbb"/>
      <g fill="var(--chart-pink)">
        <rect x="30" y="30" width="5" height="35"/><rect x="40" y="40" width="5" height="25"/>
        <rect x="190" y="25" width="5" height="40"/><rect x="200" y="35" width="5" height="30"/>
        <rect x="60" y="100" width="5" height="30"/><rect x="230" y="95" width="5" height="35"/>
      </g>
      <g fill="var(--chart-green)">
        <rect x="50" y="45" width="5" height="20"/><rect x="210" y="50" width="5" height="15"/>
        <rect x="70" y="110" width="5" height="20"/><rect x="240" y="105" width="5" height="25"/>
      </g>
    </svg>
  </div>

  <div class="chart-card">
    <svg viewBox="0 0 318 147" preserveAspectRatio="none">
      <rect x="150" y="40" width="150" height="90" fill="var(--chart-green)"/>
      <g stroke="var(--chart-pink)" stroke-width="2">
        <line x1="40" y1="60" x2="40" y2="130"/><line x1="60" y1="50" x2="60" y2="130"/>
        <line x1="80" y1="70" x2="80" y2="130"/><line x1="100" y1="45" x2="100" y2="130"/>
        <line x1="120" y1="65" x2="120" y2="130"/><line x1="140" y1="55" x2="140" y2="130"/>
      </g>
      <line x1="20" y1="130" x2="300" y2="130" stroke="#999"/>
    </svg>
  </div>

  <div class="chart-card">
    <svg viewBox="0 0 318 147" preserveAspectRatio="none">
      <rect x="0" y="0" width="318" height="147" fill="var(--chart-red)"/>
      <path d="M0 30 C100 20 200 50 318 40 L318 147 L0 147Z" fill="var(--chart-yellow)"/>
      <path d="M0 70 C100 60 200 90 318 80 L318 147 L0 147Z" fill="var(--chart-green)"/>
      <path d="M0 110 C100 100 200 125 318 118 L318 147 L0 147Z" fill="var(--chart-yellow)"/>
      <polyline points="10,55 80,65 150,75 220,90 300,95" fill="none" stroke="#222" stroke-width="2"/>
    </svg>
  </div>
</section>

<section class="panel panel--cover">
  <div class="brand">
    <span class="brand-mark"></span>
    <span class="brand-name">Velstrafield<br>Management Limited</span>
  </div>
  <div class="cover-photo" role="img" aria-label="Photo of a laptop, coffee cup and architectural plans on a desk, with a person's hands resting on the plans"></div>
  <div class="cover-band"></div>
  <h1 class="cover-title">Milestone Linked<br>Tracking <span class="accent">(MLT)</span></h1>
  <div class="cover-dots"><span></span><span></span><span></span><span></span><span></span><span></span><span></span></div>
  <p class="cover-subtitle">New Project Management Software</p>
  <address class="cover-contact">
    <strong>www.velstrafield.com</strong><br>
    info@velstrafield.com
  </address>
</section>

</body>
</html>
```